Design needed for Cover of Conference Brochure

We are a conference company that puts on several business conferences per year. We are putting together a new conference - the Clearpath Forum Week, and our audience is UX practitioners and specialists, product designers, UX designers, etc.
We need a brochure cover created. We are looking for fresh design ideas and are open to varying color schemes - please just keep in mind that this is a conference for business professionals, and fonts and colors should reflect this. Only restriction is that we do have a general cover format that we follow - i.e. which text goes where. (I've attached samples from our other events to reference.) We also generally have a central image to each brochure - feel free to submit a few versions with different images... we want something that accurately represents UX. However, if the design is compelling enough, image might not be completely necessary. We are relatively flexible - we just want something sharp!
- Must include BWKT logo (see placing on sample event covers)
- Must include footer - see sample covers
- Red text in word document are notes to you the designer - not actual text meant to appear on the cover
This cover is standard 8x11, and will be used for web only, not print. I have attached a word doc that includes all of the text that you will need for the cover. We will need final version in PDF, jpeg, and PSD. Please message me with any questions or clarification.

```html
<!DOCTYPE html>
<html lang="en">
<head>
<meta charset="utf-8">
<title>Clearpath Forum Week – Brochure Cover</title>
<link rel="stylesheet" href="https://fonts.googleapis.com/css2?family=Ubuntu:wght@700&family=Cabin:wght@500;600&family=Oswald:wght@500;600&family=Raleway:wght@400&display=swap">
<style>
  :root {
    --navy: #1c1a63;
    --navy-deep: #141248;
    --footer-blue: #1a5cb0;
    --title-yellow: #ffe600;
    --title-sky: #8cc8f0;
    --accent-red: #c1272d;
    --ink: #1d1d3a;
    --promo-yellow: #fff200;
    --sheet-top: #e4e9ef;
    --sheet-bottom: #f7f8fa;
    --badge-blue: #3aa6e8;
  }
  * { margin: 0; padding: 0; box-sizing: border-box; }
  html, body { width: 946px; height: 1200px; overflow: hidden; background: #ffffff; }
  .cover {
    position: relative;
    width: 946px; height: 1200px;
    overflow: hidden;
    background: linear-gradient(180deg, var(--sheet-top) 0%, #ffffff 45%, var(--sheet-bottom) 100%);
    font-family: "Cabin", sans-serif;
    color: var(--ink);
  }
  .shapes { position: absolute; inset: 0; }
  .title { position: absolute; left: 0; top: 58px; width: 946px; height: 100px; }
  .title text { font-family: "Ubuntu", sans-serif; font-weight: 700; font-size: 58px; letter-spacing: -1px; }
  .tagline {
    position: absolute; top: 164px; left: 0; width: 946px; text-align: center;
    font-family: "Cabin", sans-serif; font-weight: 600; font-size: 24px;
    color: var(--accent-red);
  }
  .event-date {
    position: absolute; left: 140px; top: 252px;
    font-weight: 600; font-size: 23px; color: var(--navy);
  }
  .event-venue {
    position: absolute; left: 416px; top: 248px;
    font-family: "Raleway", sans-serif; font-size: 17px; line-height: 22px; color: var(--navy);
  }
  .highlights {
    position: absolute; left: 53px; top: 802px; list-style: none;
  }
  .highlights li {
    display: flex; align-items: center; gap: 8px;
    height: 39px; font-weight: 500; font-size: 20px; color: var(--ink);
  }
  .highlights svg { width: 30px; height: 26px; flex: none; }
  .promo {
    position: absolute; right: 212px; top: 1012px; text-align: right;
    font-family: "Oswald", sans-serif; font-weight: 600; color: var(--promo-yellow);
    line-height: 1.1;
  }
  .promo .small { font-size: 20px; }
  .promo .big { font-size: 38px; line-height: 1.05; }
  .register {
    position: absolute; left: 53px; top: 1072px; color: #fff;
  }
  .register .call-to-action {
    font-family: "Oswald", sans-serif; font-weight: 500; font-size: 27px; color: var(--promo-yellow);
  }
  .register .phone {
    display: flex; align-items: center; gap: 4px;
    font-weight: 600; font-size: 30px; margin-top: 4px;
  }
  .register .web {
    display: flex; align-items: center; gap: 5px;
    font-family: "Raleway", sans-serif; font-size: 15px; margin-top: 6px;
  }
  .brand-badge {
    position: absolute; left: 790px; top: 1000px; width: 126px; height: 126px;
    background: var(--badge-blue); border: 4px solid #ffffff;
    display: flex; align-items: center; justify-content: center;
    font-family: "Cabin", sans-serif; font-weight: 600; font-size: 32px; color: #ffffff;
  }
</style>
</head>
<body>
<main class="cover">
  <svg class="shapes" width="946" height="1200" viewBox="0 0 946 1200">
    <defs>
      <linearGradient id="tabGrad" x1="0" y1="0" x2="0" y2="1">
        <stop offset="0" stop-color="#f2f3f5"/>
        <stop offset="0.3" stop-color="#c9ccd1"/>
        <stop offset="1" stop-color="#b8bcc2"/>
      </linearGradient>
      <linearGradient id="photoGrad" x1="0" y1="0" x2="1" y2="1">
        <stop offset="0" stop-color="#9db0cc"/>
        <stop offset="0.45" stop-color="#2e3644"/>
        <stop offset="1" stop-color="#7d93b3"/>
      </linearGradient>
      <linearGradient id="footerGrad" x1="0" y1="0" x2="1" y2="0">
        <stop offset="0" stop-color="var(--footer-blue)"/>
        <stop offset="0.5" stop-color="#1f3f93"/>
        <stop offset="1" stop-color="var(--navy-deep)"/>
      </linearGradient>
      <linearGradient id="promoGrad" x1="0" y1="0" x2="1" y2="0">
        <stop offset="0" stop-color="#2e2e2e"/>
        <stop offset="1" stop-color="#c4c6c9"/>
      </linearGradient>
    </defs>

    <!-- event info tab behind the hero image -->
    <path class="info-tab" d="M82,230 H735 Q752,230 756,248 L762,300 L150,300 L170,690 Q150,700 140,680 L70,250 Q68,230 82,230 Z" fill="url(#tabGrad)"/>

    <!-- hero image area -->
    <path class="hero-image" role="img" aria-label="Photo: businessman holding a laptop, tablet and phone linked by a glowing globe network of user icons"
          d="M126,303 H778 Q792,303 794,318 L853,750 Q855,766 840,766 H188 Q174,766 172,752 L112,318 Q110,303 126,303 Z"
          fill="url(#photoGrad)"/>

    <!-- promo panel -->
    <path class="promo-panel" d="M478,1004 H761 V1139 H520 Q500,1139 486,1124 L446,1046 Q436,1026 446,1014 Q456,1004 478,1004 Z" fill="url(#promoGrad)"/>

    <!-- brand block -->
    <path class="brand-block" d="M770,980 H946 V1152 H770 Q761,1152 761,1143 V989 Q761,980 770,980 Z" fill="var(--navy)"/>

    <!-- footer band -->
    <path class="footer-band" d="M0,1060 H300 C362,1060 372,1162 462,1162 H946 V1200 H0 Z" fill="url(#footerGrad)"/>
  </svg>

  <svg class="title" viewBox="0 0 946 100" aria-label="Clearpath Forum Week">
    <text x="473" y="72" text-anchor="middle" fill="none" stroke="var(--title-yellow)" stroke-width="22" stroke-linejoin="round">CLEARPATH FORUM WEEK</text>
    <text x="473" y="72" text-anchor="middle" fill="none" stroke="var(--title-sky)" stroke-width="14" stroke-linejoin="round">CLEARPATH FORUM WEEK</text>
    <text x="473" y="72" text-anchor="middle" fill="var(--navy)" stroke="#ffffff" stroke-width="6" stroke-linejoin="round" paint-order="stroke">CLEARPATH FORUM WEEK</text>
  </svg>

  <p class="tagline">Design Compelling Experiences through Successful UX Strategy</p>

  <p class="event-date">June 10-12, 2014</p>
  <p class="event-venue">Harborview Club &amp; Hotel<br>San Francisco, CA</p>

  <ul class="highlights">
    <li><svg viewBox="0 0 30 26"><rect x="1" y="7" width="18" height="17" fill="#fff" stroke="var(--accent-red)" stroke-width="2"/><path d="M5,14 L11,21 L28,2" fill="none" stroke="var(--navy)" stroke-width="4"/></svg>Case Studies from Leading Brands on Executing an Effective UX Strategy</li>
    <li><svg viewBox="0 0 30 26"><rect x="1" y="7" width="18" height="17" fill="#fff" stroke="var(--accent-red)" stroke-width="2"/><path d="M5,14 L11,21 L28,2" fill="none" stroke="var(--navy)" stroke-width="4"/></svg>Learn How UX-Driven Innovation Can Change Your Business</li>
    <li><svg viewBox="0 0 30 26"><rect x="1" y="7" width="18" height="17" fill="#fff" stroke="var(--accent-red)" stroke-width="2"/><path d="M5,14 L11,21 L28,2" fill="none" stroke="var(--navy)" stroke-width="4"/></svg>Build a Successful UX Team that Operates Strategically</li>
    <li><svg viewBox="0 0 30 26"><rect x="1" y="7" width="18" height="17" fill="#fff" stroke="var(--accent-red)" stroke-width="2"/><path d="M5,14 L11,21 L28,2" fill="none" stroke="var(--navy)" stroke-width="4"/></svg>Insights into UX Research, User Behavior, Usability Testing, Lean UX, and More</li>
  </ul>

  <div class="promo">
    <div class="small">Register by</div>
    <div class="small">March 7th, 2014 and</div>
    <div class="big">save $400!</div>
  </div>

  <div class="brand-badge">BWKT</div>

  <div class="register">
    <p class="call-to-action">Register Today!</p>
    <p class="phone">
      <svg width="26" height="26" viewBox="0 0 26 26"><circle cx="13" cy="13" r="11.5" fill="none" stroke="#fff" stroke-width="2"/><path d="M10,6 L12,10 L10,12 Q11,15 14,17 L16,15 L20,17 L18,20 Q10,20 7,10 Z" fill="#fff"/></svg>
      888.555.0142
    </p>
    <p class="web">
      <svg width="16" height="16" viewBox="0 0 16 16" fill="none" stroke="#fff" stroke-width="1.2"><circle cx="8" cy="8" r="7"/><ellipse cx="8" cy="8" rx="3" ry="7"/><path d="M1,8 H15 M2.5,4.5 H13.5 M2.5,11.5 H13.5"/></svg>
      www.clearpathforumweek.com
    </p>
  </div>
</main>
</body>
</html>
```